For a German comparison website comparing the best online trading brokers I need 10 banners for Facebook advertising. The banners should be a size of 1200x628 with one of the following texts:
1) Traden für Anfänger
25 Euro gratis
2) Traden Sie online
25 Euro gratis
3) Online-Trading für Anfänger
4) Trading für Einsteiger
25 Euro gratis
5) Aktien für Einsteiger
25 Euro gratis
The targeted website is www.borsivolta.ch and it compares brokers where traders can trade shares, commodities,indices and Forex.

```html
<!DOCTYPE html>
<html lang="de">
<head>
<meta charset="utf-8">
<title>Trading Banner – Borsivolta</title>
<link rel="stylesheet" href="https://fonts.googleapis.com/css2?family=Arimo:wght@400;700&display=swap">
<style>
  :root {
    --page: #ffffff;
    --olive-dark: #4d6a2c;
    --olive: #6b8a3a;
    --lime: #9fbd52;
    --teal-tint: #5f8f6a;
    --box: #2e3d1c;
    --orange: #e98a0f;
    --white: #ffffff;
    --brand: #7a7a7a;
    --photo-light: #c9d3dc;
    --photo-dark: #3a4656;
  }
  html, body {
    margin: 0;
    padding: 0;
    width: 1200px;
    height: 1200px;
    overflow: hidden;
    background: var(--page);
    font-family: "Arimo", Arial, sans-serif;
  }
  .sheet {
    position: relative;
    width: 1200px;
    height: 1200px;
  }
  .banner {
    position: absolute;
    left: 118px;
    width: 960px;
    height: 502px;
    display: block;
    outline: 1px solid #222;
  }
  .banner--first { top: 101px; }
  .banner--second { top: 637px; }
  .headline { font-family: "Arimo", Arial, sans-serif; font-weight: 700; fill: var(--white); }
  .offer { font-family: "Arimo", Arial, sans-serif; font-weight: 700; fill: var(--orange); }
  .brand-name { font-family: "Arimo", Arial, sans-serif; font-weight: 700; fill: var(--brand); }
</style>
</head>
<body>
<div class="sheet">

  <svg class="banner banner--first" viewBox="0 0 1200 627" xmlns="http://www.w3.org/2000/svg">
    <defs>
      <linearGradient id="backdropBase" x1="0" y1="0" x2="0" y2="1">
        <stop offset="0" stop-color="var(--olive-dark)"/>
        <stop offset=".5" stop-color="var(--olive)"/>
        <stop offset="1" stop-color="var(--lime)"/>
      </linearGradient>
      <radialGradient id="backdropGlow" cx=".45" cy=".2" r=".6">
        <stop offset="0" stop-color="var(--teal-tint)" stop-opacity=".8"/>
        <stop offset="1" stop-color="var(--teal-tint)" stop-opacity="0"/>
      </radialGradient>
      <linearGradient id="photoFill" x1="0" y1="0" x2="1" y2="1">
        <stop offset="0" stop-color="var(--photo-light)"/>
        <stop offset="1" stop-color="var(--photo-dark)"/>
      </linearGradient>
    </defs>
    <g class="market-backdrop" role="img" aria-label="Hintergrund: Börsenchart mit Kursverlauf auf grünem Raster">
      <rect width="1200" height="627" fill="url(#backdropBase)"/>
      <rect width="1200" height="627" fill="url(#backdropGlow)"/>
    </g>
    <path class="offer-panel" d="M545 395 Q870 440 1200 392 L1200 627 L590 627 Q560 520 545 395 Z" fill="var(--white)"/>
    <path class="offer-rule" d="M545 392 Q870 438 1200 390" fill="none" stroke="var(--orange)" stroke-width="8"/>
    <circle class="portrait-frame" cx="312" cy="374" r="232" fill="var(--white)"/>
    <circle cx="312" cy="374" r="224" fill="url(#photoFill)" role="img" aria-label="Foto: Frau im Business-Anzug arbeitet am Laptop in einem hellen Büro"/>
    <g class="headline-box">
      <rect x="615" y="190" width="555" height="194" rx="6" fill="var(--box)" opacity=".6"/>
      <path d="M625 210V200H645M1140 200H1160V210M1160 364V374H1140M645 374H625V364" fill="none" stroke="var(--white)" stroke-width="1.5" opacity=".7"/>
      <text class="headline" x="892" y="269" font-size="74" text-anchor="middle">Traden Für</text>
      <text class="headline" x="892" y="349" font-size="74" text-anchor="middle">Anfänger</text>
    </g>
    <text class="offer" x="868" y="500" font-size="78" text-anchor="middle" transform="rotate(-2.5 868 480)">25 EURO GRATIS</text>
    <text class="brand-name" x="1157" y="597" font-size="40" text-anchor="end">BORSIVOLTA</text>
  </svg>

  <svg class="banner banner--second" viewBox="0 0 1200 627" xmlns="http://www.w3.org/2000/svg">
    <g class="market-backdrop" role="img" aria-label="Hintergrund: Börsenchart mit Kursverlauf auf grünem Raster">
      <rect width="1200" height="627" fill="url(#backdropBase)"/>
      <rect width="1200" height="627" fill="url(#backdropGlow)"/>
    </g>
    <path class="offer-panel" d="M545 395 Q870 440 1200 392 L1200 627 L590 627 Q560 520 545 395 Z" fill="var(--white)"/>
    <path class="offer-rule" d="M545 392 Q870 438 1200 390" fill="none" stroke="var(--orange)" stroke-width="8"/>
    <circle class="portrait-frame" cx="312" cy="374" r="232" fill="var(--white)"/>
    <circle cx="312" cy="374" r="224" fill="url(#photoFill)" role="img" aria-label="Foto: Frau im Business-Anzug arbeitet am Laptop in einem hellen Büro"/>
    <g class="headline-box">
      <rect x="615" y="190" width="555" height="194" rx="6" fill="var(--box)" opacity=".6"/>
      <path d="M625 210V200H645M1140 200H1160V210M1160 364V374H1140M645 374H625V364" fill="none" stroke="var(--white)" stroke-width="1.5" opacity=".7"/>
      <text class="headline" x="892" y="272" font-size="78" text-anchor="middle">Traden Sie</text>
      <text class="headline" x="892" y="352" font-size="78" text-anchor="middle">Online</text>
    </g>
    <text class="offer" x="868" y="500" font-size="78" text-anchor="middle" transform="rotate(-2.5 868 480)">25 EURO GRATIS</text>
    <text class="brand-name" x="1157" y="597" font-size="40" text-anchor="end">BORSIVOLTA</text>
  </svg>

</div>
</body>
</html>
```